Business Card Design

Hoping for a black background business card, minimalistic design.
With the Copper Lantern logo you created in white.

I would like to include:
My Name and title
Address (street address)
Reception: (phone number)
Fax: (fax number)
Reception: (email address)
Direct email: (email address)
Instagram: (ig handle)

```html
<!DOCTYPE html>
<html lang="en">
<head>
<meta charset="utf-8">
<title>Copper Lantern — Business Card</title>
<link href="https://fonts.googleapis.com/css2?family=Open+Sans:wght@400;600;700&display=swap" rel="stylesheet">
<style>
  :root{
    --backdrop:#3b3b3d;
    --card:#111112;
    --card-edge:#1b1b1c;
    --ink:#f4f4f4;
    --ink-soft:#b9b9b9;
    --ink-muted:#7d7d7d;
    --rule:#cfcfcf;
    --icon-cut:#111112;
  }
  *{margin:0;padding:0;box-sizing:border-box}
  html,body{width:1200px;height:801px;overflow:hidden}
  body{
    background:var(--backdrop);
    font-family:"Open Sans",Arial,sans-serif;
    color:var(--ink);
    position:relative;
  }
  .card{
    position:absolute;
    top:257px;
    width:500px;
    height:286px;
    background:var(--card);
    border:1px solid var(--card-edge);
    box-shadow:0 10px 30px rgba(0,0,0,.35);
    overflow:hidden;
  }
  .card--front{left:70px}
  .card--back{left:630px}

  /* brand lockup */
  .brand{
    position:absolute;
    display:flex;
    align-items:center;
    gap:12px;
    white-space:nowrap;
  }
  .brand__circle{
    width:40px;height:40px;
    border:3px solid var(--ink);
    border-radius:50%;
    flex:none;
  }
  .brand__divider{width:1px;height:40px;background:var(--ink-soft);flex:none}
  .brand__name{
    font-weight:600;
    font-size:19px;
    letter-spacing:2.5px;
    text-transform:uppercase;
    color:var(--ink);
  }
  .card--front .brand{top:34px;right:30px}
  .rule-long{
    position:absolute;top:94px;right:30px;width:290px;height:1px;background:var(--rule);
  }

  .address{
    position:absolute;top:108px;right:30px;
    text-align:right;font-size:12.5px;line-height:1.45;color:var(--ink);
    font-style:normal;
  }

  .person{position:absolute;left:30px;top:112px}
  .person__name{font-weight:700;font-size:17px;line-height:1.3;letter-spacing:.5px;text-transform:uppercase}
  .person__title{font-size:12.5px;line-height:1.35;color:var(--ink-soft)}
  .person__rule{width:150px;height:1px;background:var(--rule);margin:7px 0 6px}

  .contacts{list-style:none;font-size:12px;line-height:1.45}
  .contacts li{display:flex;align-items:center;gap:7px;white-space:nowrap}
  .contacts svg{width:10px;height:10px;flex:none;fill:var(--ink)}
  .contacts .note{color:var(--ink-muted);font-size:10px;margin-left:3px}

  /* back */
  .pattern{
    position:absolute;inset:0;
    background:radial-gradient(ellipse at 70% 40%, #1e1e20 0%, #121213 55%, #0c0c0d 100%);
  }
  .card--back .brand{top:118px;right:40px}
</style>
</head>
<body>

<section class="card card--front" aria-label="Business card front">
  <div class="brand">
    <span class="brand__circle"></span>
    <span class="brand__divider"></span>
    <span class="brand__name">Copper Lantern</span>
  </div>
  <div class="rule-long"></div>

  <address class="address">
    845 Harbor Lane, Suite 210<br>Portland, OR 97205
  </address>

  <div class="person">
    <div class="person__name">Daniel Reyes</div>
    <div class="person__title">President</div>
    <div class="person__rule"></div>
    <ul class="contacts">
      <li><svg viewBox="0 0 10 10"><path d="M2 0.5 3.6 2.6 2.7 3.6C3.3 5 4.8 6.6 6.4 7.3L7.4 6.4 9.5 8 8.3 9.5C4.3 9 1 5.7 0.5 1.7Z"/></svg>202.555.0147<span class="note">(Reception)</span></li>
      <li><svg viewBox="0 0 10 10"><rect x="2.5" y="0.5" width="5" height="3"/><rect x="0.5" y="4" width="9" height="4.5" rx="1"/></svg>202.555.0147<span class="note">(Fax)</span></li>
      <li><svg viewBox="0 0 10 10"><path d="M0.5 2h9v6h-9z M0.5 2 5 5.5 9.5 2" stroke="var(--icon-cut)" stroke-width=".8"/></svg>info@copperlantern.com<span class="note">(Reception)</span></li>
      <li><svg viewBox="0 0 10 10"><path d="M0.5 2h9v6h-9z M0.5 2 5 5.5 9.5 2" stroke="var(--icon-cut)" stroke-width=".8"/></svg>daniel@copperlantern.com<span class="note">(Direct)</span></li>
      <li><svg viewBox="0 0 10 10"><circle cx="5" cy="5" r="4.5"/><path d="M0.5 5h9M5 0.5c-2 2.5-2 6.5 0 9M5 0.5c2 2.5 2 6.5 0 9" stroke="var(--icon-cut)" stroke-width=".7" fill="none"/></svg>www.copperlantern.com</li>
    </ul>
  </div>
</section>

<section class="card card--back" aria-label="Business card back">
  <div class="pattern" role="img" aria-label="Embossed repeating brand pattern in gloss black"></div>
  <div class="brand">
    <span class="brand__circle"></span>
    <span class="brand__divider"></span>
    <span class="brand__name">Copper Lantern</span>
  </div>
</section>

</body>
</html>
```